FernMill Coatings website development for protective coatings manufacturer

We require a website for a new company which manufacturers protective coatings for automotive and industrial applications. We have a new logo which can be used and will be uploaded for inclusion on the website. There should be the following pages:
Home
About us
Products
Distribution
Contact us
There will be 10 products with downloadable pdf files TDS and MSDS.
Target Market(s)
Automotive and industrial coatings
Industry/Entity Type
Protective Coatings manufacturing
Coding
Coded - Design and coding required
Font styles to use
Sans Serif
Requirements
Must have
- Nice and clear images related to the target market

```html
<!DOCTYPE html>
<html lang="en">
<head>
<meta charset="utf-8">
<title>FernMill Coatings</title>
<link href="https://fonts.googleapis.com/css2?family=Poppins:wght@600;700&family=Tinos:wght@400;700&display=swap" rel="stylesheet">
<style>
:root{
  --brand:#285a8c;
  --brand-dark:#1f4a75;
  --ink:#111;
  --text:#333;
  --white:#fff;
  --black:#000;
  --star:#f5e12a;
}
*{box-sizing:border-box;margin:0;padding:0}
html,body{width:1200px;height:3181px;overflow:hidden}
body{position:relative;background:var(--white);font-family:"Tinos",serif;color:var(--text)}
.abs{position:absolute}
.heading{font-family:"Poppins",sans-serif;font-weight:700;color:var(--ink)}
.btn{display:inline-block;background:var(--brand);color:var(--white);font-size:15px;text-align:center}

/* header */
.site-header{left:0;top:0;width:1200px;height:116px;background:var(--white)}
.brand{left:111px;top:40px;display:flex;align-items:center;gap:10px;font-family:"Poppins",sans-serif;font-weight:700;font-size:26px;color:var(--brand)}
.brand-mark{width:18px;height:18px;background:var(--brand)}
.contact-item{display:flex;gap:14px;align-items:flex-start;font-size:14px;line-height:26px;color:#333}
.contact-item svg{margin-top:12px;flex:none}

/* nav */
.main-nav{left:111px;top:116px;width:977px;height:60px;background:var(--brand);display:flex;justify-content:center;align-items:center;gap:56px;z-index:2}
.main-nav a{color:var(--white);font-size:16px;text-decoration:none}

/* hero */
.hero{left:0;top:116px;width:1200px;height:652px;background:linear-gradient(90deg,#f1f3f6 0%,#e9ecf0 45%,#cfd3d8 70%,#b9bec4 100%)}
.hero-title{left:111px;top:258px;font-size:62px;line-height:86px}
.hero-text{left:111px;top:436px;width:545px;font-size:19px;line-height:30px;color:#222}
.hero-btn{left:111px;top:587px;width:115px;height:43px;line-height:43px}
.dots{left:579px;top:711px;display:flex;gap:3px}
.dots span{width:7px;height:7px;background:#111}
.dots span.on{width:10px;height:8px;background:var(--brand)}

/* about */
.about-photo-a{left:111px;top:853px;width:437px;height:421px;background:linear-gradient(135deg,#c8ccd2,#8c97a3 55%,#3a4656)}
.about-photo-a::after{content:"";position:absolute;left:0;bottom:0;width:140px;height:160px;background:linear-gradient(#f2a54a,#b96515)}
.about-photo-b{left:252px;top:1115px;width:330px;height:198px;background:linear-gradient(135deg,#6f9bd6,#2f5f9e 60%,#173a6b);border-left:4px solid var(--white);border-top:4px solid var(--white)}
.about-title{left:617px;top:868px;font-size:37px}
.about-text{left:617px;top:936px;width:430px;font-size:14px;line-height:26px;color:#333}
.about-text p+p{margin-top:11px}
.about-btn{left:617px;top:1241px;width:115px;height:43px;line-height:43px}

/* products */
.products-title{left:111px;top:1388px;font-size:37px}
.arrow{width:40px;height:40px;border-radius:50%;background:var(--brand);display:flex;align-items:center;justify-content:center}
.card{top:1497px;width:299px;height:456px;background:var(--brand);text-align:center;color:var(--white)}
.card-img{width:299px;height:241px;position:relative}
.card-img .cart{position:absolute;right:14px;bottom:16px}
.card-name{font-family:"Poppins",sans-serif;font-weight:700;font-size:21px;line-height:34px;margin-top:10px;padding:0 20px}
.stars{display:flex;justify-content:center;gap:1px;margin-top:4px}
.price{font-family:"Poppins",sans-serif;font-weight:700;font-size:17px;margin-top:4px}
.docs{display:flex;justify-content:center;gap:12px;margin-top:20px}
.doc{width:115px;height:43px;background:var(--white);color:var(--brand);font-size:15px;display:flex;align-items:center;justify-content:center;gap:10px}

/* distribution */
.distribution{left:0;top:2040px;width:1200px;height:481px;background:linear-gradient(90deg,#2a2e33,#3b4046 40%,#2c3438 70%,#1d3a3e)}
.dist-title{left:0;top:2088px;width:1200px;text-align:center;font-size:37px;color:var(--white)}
.dist-text{left:275px;top:2160px;width:650px;text-align:center;font-size:14px;line-height:26px;color:var(--white)}
.dist-text p+p{margin-top:20px}
.dist-btn{left:543px;top:2422px;width:115px;height:43px;line-height:43px}

/* footer */
.site-footer{left:0;top:2710px;width:1200px;height:471px;background:var(--black)}
.newsletter{left:185px;top:2606px;width:830px;height:207px;background:var(--white);box-shadow:0 0 14px rgba(0,0,0,.15);text-align:center}
.newsletter h2{font-size:37px;margin-top:36px}
.subscribe{display:flex;margin:20px auto 0;width:513px;height:46px}
.subscribe .field{flex:1;border:2px solid var(--brand);border-right:none;font-size:12px;text-align:left;padding-left:20px;line-height:42px;color:#222}
.subscribe .go{width:116px;background:var(--brand);color:var(--white);font-size:15px;line-height:46px}
.footer-brand{left:0;top:2915px;width:1200px;text-align:center;font-family:"Poppins",sans-serif;font-weight:700;font-size:38px;color:var(--white)}
.footer-nav{left:0;top:3012px;width:1200px;display:flex;justify-content:center;gap:18px;font-size:15px;color:var(--white)}
.social{left:0;top:3062px;width:1200px;display:flex;justify-content:center;gap:20px}
.social span{width:22px;height:22px;border-radius:3px;background:var(--white)}
.rule{left:0;top:3124px;width:1200px;height:1px;background:#444}
.copyright{left:0;top:3143px;width:1200px;text-align:center;font-size:13px;color:var(--white)}
</style>
</head>
<body>

<header class="abs site-header">
  <div class="abs brand"><span class="brand-mark"></span>FernMill Coatings</div>
  <div class="abs contact-item" style="left:385px;top:26px">
    <svg width="28" height="28" viewBox="0 0 24 24"><path fill="#285a8c" d="M6.6 10.8a15 15 0 0 0 6.6 6.6l2.2-2.2a1 1 0 0 1 1-.25 11.4 11.4 0 0 0 3.6.57 1 1 0 0 1 1 1V20a1 1 0 0 1-1 1A17 17 0 0 1 3 4a1 1 0 0 1 1-1h3.5a1 1 0 0 1 1 1c0 1.25.2 2.45.57 3.57a1 1 0 0 1-.25 1z"/></svg>
    <div>Call Us: +07 555 014 208<br>info@fernmillcoatings.com</div>
  </div>
  <div class="abs contact-item" style="left:639px;top:26px">
    <svg width="30" height="30" viewBox="0 0 24 24"><circle cx="12" cy="12" r="10" fill="none" stroke="#285a8c" stroke-width="2"/><path d="M12 6v6l4 2" fill="none" stroke="#285a8c" stroke-width="2"/></svg>
    <div>Mon - Fri: 9.00am -8.00pm<br>Sat &amp; Sun Closed</div>
  </div>
  <div class="abs contact-item" style="left:894px;top:26px">
    <svg width="26" height="32" viewBox="0 0 24 30"><path fill="#285a8c" d="M12 0a10 10 0 0 0-10 10c0 7.5 10 20 10 20s10-12.5 10-20A10 10 0 0 0 12 0zm0 14a4 4 0 1 1 0-8 4 4 0 0 1 0 8z"/></svg>
    <div>42, Fernmill Works<br>Automotive, Na 510247.</div>
  </div>
</header>

<nav class="abs main-nav">
  <a>Home</a><a>About us</a><a>Products</a><a>Distribution</a><a>Contact us</a>
</nav>

<section class="abs hero" role="img" aria-label="Painter in protective suit and respirator holding a spray gun in a spray booth"></section>
<h1 class="abs heading hero-title">Welcome to<br>FernMill Coatings</h1>
<p class="abs hero-text">Lorem ipsum dolor sit amet, consectetur adipiscing elit, sed do eiusmod tempor incididunt ut labore et dolore magna aliqua. Ut enim ad minim veniam, quis nostrud exercitation ullamco laboris ut aliquip ex ea commodo consequat.</p>
<a class="abs btn hero-btn">Read More</a>
<div class="abs dots"><span class="on"></span><span></span><span></span><span></span></div>

<div class="abs about-photo-a" role="img" aria-label="Worker in respirator spraying coating inside a booth"></div>
<div class="abs about-photo-b" role="img" aria-label="Technician in protective suit beside a masked car body, blue tinted"></div>
<h2 class="abs heading about-title">About Us</h2>
<div class="abs about-text">
  <p>Duis aute irure dolor in reprehenderit in voluptate velit esse cillum dolore eu fugiat nulla pariatur. Excepteur sint occaecat cupidatat non proident, sunt in culpa qui officia deserunt mollit anim id est laborum.</p>
  <p>Sed ut perspiciatis unde omnis iste natus error sit voluptatem accusantium doloremque laudantium, totam rem aperiam, eaque ipsa quae ab illo inventore veritatis et quasi architecto beatae vitae dicta sunt explicabo. Nemo enim ipsam voluptatem quia voluptas sit aspernatur aut odit aut fugit, sed quia consequuntur magni dolores eos qui ratione voluptatem sequi nesciunt.</p>
</div>
<a class="abs btn about-btn">Read More</a>

<h2 class="abs heading products-title">Our Products</h2>
<div class="abs arrow" style="left:992px;top:1400px"><svg width="14" height="14" viewBox="0 0 14 14"><path d="M9 2 4 7l5 5" fill="none" stroke="#fff" stroke-width="2.4"/></svg></div>
<div class="abs arrow" style="left:1047px;top:1400px"><svg width="14" height="14" viewBox="0 0 14 14"><path d="m5 2 5 5-5 5" fill="none" stroke="#fff" stroke-width="2.4"/></svg></div>

<article class="abs card" style="left:113px">
  <div class="card-img" role="img" aria-label="White paint tin on grey tiled floor" style="background:radial-gradient(circle at 50% 50%,#e6e6e6 0 28%,#8a8a8a 60%,#6a6a6a)">
    <svg class="cart" width="34" height="26" viewBox="0 0 34 26"><path d="M1 2h5l4 16h18l4-12H8" fill="none" stroke="#fff" stroke-width="2"/><circle cx="13" cy="23" r="2" fill="#fff"/><circle cx="26" cy="23" r="2" fill="#fff"/></svg>
  </div>
  <div class="card-name">Sed ut perspiciatis unde</div>
  <div class="stars"><svg width="76" height="14" viewBox="0 0 76 14" fill="#f5e12a"><path id="s" d="M7 0l2 4.5 5 .5-3.8 3.3 1.1 5L7 10.8 2.7 13.3l1.1-5L0 5l5-.5z"/><use href="#s" x="15.5"/><use href="#s" x="31"/><use href="#s" x="46.5"/><use href="#s" x="62"/></svg></div>
  <div class="price">$500.00</div>
  <div class="docs"><span class="doc">TDS <svg width="22" height="24" viewBox="0 0 22 24"><rect x="4" y="1" width="15" height="20" fill="none" stroke="#333" stroke-width="1.5"/><rect x="1" y="8" width="14" height="7" fill="none" stroke="#333" stroke-width="1.5"/></svg></span><span class="doc">MSDS <svg width="22" height="24" viewBox="0 0 22 24"><rect x="4" y="1" width="15" height="20" fill="none" stroke="#333" stroke-width="1.5"/><rect x="1" y="8" width="14" height="7" fill="none" stroke="#333" stroke-width="1.5"/></svg></span></div>
</article>

<article class="abs card" style="left:451px">
  <div class="card-img" role="img" aria-label="White paint can on dark blue misty background" style="background:radial-gradient(circle at 50% 50%,#e8ecf0 0 26%,#1e3552 58%,#0b1626)">
    <svg class="cart" width="34" height="26" viewBox="0 0 34 26"><path d="M1 2h5l4 16h18l4-12H8" fill="none" stroke="#fff" stroke-width="2"/><circle cx="13" cy="23" r="2" fill="#fff"/><circle cx="26" cy="23" r="2" fill="#fff"/></svg>
  </div>
  <div class="card-name">Lorem ipsum dolor sit amet</div>
  <div class="stars"><svg width="76" height="14" viewBox="0 0 76 14" fill="#f5e12a"><use href="#s"/><use href="#s" x="15.5"/><use href="#s" x="31"/><use href="#s" x="46.5"/><use href="#s" x="62"/></svg></div>
  <div class="price">$400.00</div>
  <div class="docs"><span class="doc">TDS <svg width="22" height="24" viewBox="0 0 22 24"><rect x="4" y="1" width="15" height="20" fill="none" stroke="#333" stroke-width="1.5"/><rect x="1" y="8" width="14" height="7" fill="none" stroke="#333" stroke-width="1.5"/></svg></span><span class="doc">MSDS <svg width="22" height="24" viewBox="0 0 22 24"><rect x="4" y="1" width="15" height="20" fill="none" stroke="#333" stroke-width="1.5"/><rect x="1" y="8" width="14" height="7" fill="none" stroke="#333" stroke-width="1.5"/></svg></span></div>
</article>

<article class="abs card" style="left:789px">
  <div class="card-img" role="img" aria-label="White paint tin on wooden surface with dark smoky backdrop" style="background:radial-gradient(circle at 50% 48%,#e6e6e6 0 26%,#2a2a2a 58%,#4a2f1e)">
    <svg class="cart" width="34" height="26" viewBox="0 0 34 26"><path d="M1 2h5l4 16h18l4-12H8" fill="none" stroke="#fff" stroke-width="2"/><circle cx="13" cy="23" r="2" fill="#fff"/><circle cx="26" cy="23" r="2" fill="#fff"/></svg>
  </div>
  <div class="card-name">Sed ut perspiciatis unde</div>
  <div class="stars"><svg width="76" height="14" viewBox="0 0 76 14" fill="#f5e12a"><use href="#s"/><use href="#s" x="15.5"/><use href="#s" x="31"/><use href="#s" x="46.5"/><use href="#s" x="62"/></svg></div>
  <div class="price">$500.00</div>
  <div class="docs"><span class="doc">TDS <svg width="22" height="24" viewBox="0 0 22 24"><rect x="4" y="1" width="15" height="20" fill="none" stroke="#333" stroke-width="1.5"/><rect x="1" y="8" width="14" height="7" fill="none" stroke="#333" stroke-width="1.5"/></svg></span><span class="doc">MSDS <svg width="22" height="24" viewBox="0 0 22 24"><rect x="4" y="1" width="15" height="20" fill="none" stroke="#333" stroke-width="1.5"/><rect x="1" y="8" width="14" height="7" fill="none" stroke="#333" stroke-width="1.5"/></svg></span></div>
</article>

<section class="abs distribution" role="img" aria-label="Dark workshop scene of a gloved hand sanding a car panel"></section>
<h2 class="abs heading dist-title">Distribution</h2>
<div class="abs dist-text">
  <p>Nemo enim ipsam voluptatem quia voluptas sit aspernatur aut odit aut fugit, sed quia consequuntur magni dolores eos qui ratione voluptatem sequi nesciunt. Neque porro quisquam est, qui dolorem ipsum quia dolor sit amet, consectetur, adipisci velit, sed quia non numquam eius modi tempora incidunt ut labore et dolore magnam aliquam quaerat voluptatem.</p>
  <p>Lorem ipsum dolor sit amet, consectetur adipiscing elit, sed do eiusmod tempor incididunt ut labore et dolore magna aliqua. Ut enim ad minim veniam, quis nostrud exercitation ullamco laboris nisi ut aliquip ex ea commodo consequat. Duis aute irure dolor in reprehenderit in voluptate velit esse cillum dolore eu fugiat nulla pariatur.</p>
</div>
<a class="abs btn dist-btn">Learn More</a>

<footer class="abs site-footer"></footer>
<div class="abs newsletter">
  <h2 class="heading">Subscribe Newsletter</h2>
  <div class="subscribe"><span class="field">Enter Your Email</span><span class="go">Subscribe</span></div>
</div>
<div class="abs footer-brand">FernMill Coatings</div>
<div class="abs footer-nav"><span>Home</span><span>|</span><span>About us</span><span>|</span><span>Products</span><span>|</span><span>Distribution</span><span>|</span><span>Contact us</span></div>
<div class="abs social"><span></span><span></span><span></span></div>
<div class="abs rule"></div>
<div class="abs copyright">Copyright © 2023 FernMill Coatings. All Rights Reserved.</div>

</body>
</html>
```